Packaging Artwork for "Earth's First Expanding Biodisposable Loofah Pads"

Our company manufactures BrisaPods. They are Earth's first expanding, biodisposable loofah pads for exfoliating the skin.
BrisaPods are biodisposable, so they can be thrown-away (or composted) before nasty skin bacteria can grow on them. This makes scrubbing skin cleaner and safer.
This is a high-end product, so our packaging needs to be very clean, sophisticated and make our product look like it should be expensive. The packaging should also let the viewer know the product is environmentally friendly.
The product name is "BrisaPods". The packaging also has to say "Biodisposable".
Our new packaging is a hanging bag with a window in it. See the image attached. There is also a picture of our current packaging for our Tarnivelles sponges. We would like completely different artwork, but keep the white paper.
The attached images are of our kitchen cleaning pads "Quorlimates". This new packaging is for "BrisaPods" which are a beauty product and the artwork must be different. Also, the packaging should have a large image of the round loofah pad on the front and the image of the loofah expanding from thin to thick on the back.
Updates

This will be a 4-inch x 4-inch bag that will hang from a hook. The bag will be about 2-inches thick. The logo will be similar to the Quorlimates fish logo that has been added to the project. Instead of saying "tarnivelles", the word "BrisaPods" needs to be used in the logo.

Industry/Entity Type

health and beauty

Requirements
Must have
• slogan "Clean Germ Free. Guilt Free". The product should be called "Earth's First Expanding Biodisposable Bath Loofahs". simple clean design on a white background. see the picture of our current packaging below. We will use the same paper. We just need completely different, sophisticated artwork

```html
<!DOCTYPE html>
<html lang="en">
<head>
<meta charset="utf-8">
<title>BrisaPods – Earth's First Expanding Biodisposable Bath Loofahs</title>
<link rel="stylesheet" href="https://fonts.googleapis.com/css2?family=Barlow:wght@500;600;700&display=swap">
<style>
  :root {
    --green-light: #36a234;
    --green: #1a8a3a;
    --green-dark: #066a2c;
    --teal: #1f8f9c;
    --ink: #5a4747;
    --white: #ffffff;
    --paper: #fbfbfb;
    --shadow-grey: #8b9798;
    --loofah-light: #efe3cc;
    --loofah: #dccaa6;
    --loofah-dark: #c7b188;
  }
  html, body {
    margin: 0;
    padding: 0;
    width: 846px;
    height: 1200px;
    overflow: hidden;
    background: var(--paper);
  }
  .label {
    position: relative;
    width: 846px;
    height: 1200px;
    background: var(--white);
    font-family: "Barlow", sans-serif;
  }
  .top-band {
    position: absolute;
    left: 0; top: 0;
    width: 100%; height: 132px;
    background: linear-gradient(90deg, var(--green-light), var(--green) 45%, var(--green-dark));
    border-bottom: 11px solid var(--teal);
  }
  .claim {
    position: absolute;
    left: 53px; top: 72px;
    color: var(--white);
    font-weight: 700;
    font-size: 27px;
    line-height: 32px;
    letter-spacing: 1.5px;
  }
  .count {
    position: absolute;
    right: 34px; top: 62px;
    display: flex;
    align-items: center;
    color: var(--white);
  }
  .count-number {
    font-weight: 700;
    font-size: 60px;
    line-height: 1;
    margin-right: 10px;
  }
  .count-text {
    font-weight: 700;
    font-size: 17px;
    line-height: 18px;
    letter-spacing: 1.2px;
    text-transform: uppercase;
  }
  .count-text small {
    display: block;
    font-size: 11px;
    line-height: 13px;
    letter-spacing: 1px;
  }
  .brand {
    position: absolute;
    left: 0; top: 272px;
    width: 100%;
    display: flex;
    justify-content: center;
    align-items: center;
    gap: 16px;
  }
  .brand-dot {
    width: 46px; height: 46px;
    border-radius: 50%;
    background: var(--teal);
  }
  .brand-name {
    color: var(--ink);
    font-weight: 600;
    font-size: 68px;
    line-height: 1;
  }
  .product-kicker {
    position: absolute;
    left: 0; top: 494px;
    width: 100%;
    margin: 0;
    text-align: center;
    color: var(--green-dark);
    font-weight: 600;
    font-size: 27px;
    line-height: 34px;
    letter-spacing: 1px;
  }
  .product-title {
    position: absolute;
    left: 0; top: 532px;
    width: 100%;
    margin: 0;
    text-align: center;
    color: var(--green-dark);
    font-weight: 700;
    font-size: 43px;
    line-height: 52px;
    letter-spacing: 1px;
  }
  .product-photo {
    position: absolute;
    left: 118px; top: 603px;
    width: 617px; height: 341px;
    border-radius: 50%;
    background: radial-gradient(ellipse at 45% 40%, var(--loofah-light), var(--loofah) 60%, var(--loofah-dark));
  }
  .features {
    position: absolute;
    left: 92px; top: 958px;
    width: 658px; height: 76px;
    background: linear-gradient(90deg, var(--green-dark), var(--green) 50%, var(--green-dark));
    display: flex;
    align-items: center;
  }
  .feature {
    position: relative;
    flex: 1;
    text-align: center;
    color: var(--white);
    font-weight: 600;
    font-size: 21px;
    line-height: 28px;
    letter-spacing: 0.8px;
  }
  .feature + .feature { border-left: 2px solid var(--white); }
  .feature-icon {
    position: absolute;
    left: 50%; top: -68px;
    width: 44px; height: 44px;
    transform: translateX(-50%);
    z-index: 2;
  }
  .tagline {
    position: absolute;
    left: 219px; top: 1018px;
    width: 414px;
    padding: 8px 0 8px 40px;
    box-sizing: border-box;
    background: var(--teal);
    box-shadow: -5px 5px 0 var(--shadow-grey);
    transform: rotate(-2deg);
    color: var(--white);
    font-weight: 700;
    font-size: 18px;
    line-height: 20px;
    letter-spacing: 0.5px;
  }
  .bottom-band {
    position: absolute;
    left: 0; top: 1125px;
    width: 100%; height: 62px;
    background: linear-gradient(90deg, var(--green-dark), var(--green) 50%, var(--green-dark));
    border-top: 13px solid var(--teal);
  }
  .slogan {
    margin: 0;
    text-align: center;
    line-height: 62px;
    color: var(--white);
    font-weight: 600;
    font-size: 28px;
    letter-spacing: 1px;
  }
</style>
</head>
<body>
  <main class="label">
    <header class="top-band">
      <div class="claim">BIODISPOSABLE</div>
      <div class="count">
        <span class="count-number">12</span>
        <span class="count-text">Expanding<br>Bath Loofahs<small>3 Month Supply</small></span>
      </div>
    </header>

    <div class="brand">
      <span class="brand-dot"></span>
      <span class="brand-name">BrisaPods</span>
    </div>

    <p class="product-kicker">EARTH'S FIRST EXPANDING</p>
    <h1 class="product-title">BIODISPOSABLE BATH LOOFAHS</h1>

    <div class="product-photo" role="img" aria-label="Close-up photo of a round natural bath loofah pad"></div>

    <div class="features">
      <div class="feature">
        <svg class="feature-icon" viewBox="0 0 46 46" aria-hidden="true">
          <path d="M23 44 V22" stroke="var(--green)" stroke-width="4" fill="none"/>
          <path d="M23 24 C10 24 4 14 5 6 C15 6 23 12 23 24 Z" fill="var(--green)"/>
          <path d="M23 22 C34 22 42 14 41 8 C31 8 23 12 23 22 Z" fill="var(--green)"/>
        </svg>
        ALL PLANT
      </div>
      <div class="feature">
        <svg class="feature-icon" viewBox="0 0 46 46" aria-hidden="true">
          <rect x="3" y="13" width="8" height="20" rx="2" fill="var(--green)"/>
          <rect x="35" y="13" width="8" height="20" rx="2" fill="var(--green)"/>
          <rect x="11" y="20" width="24" height="6" fill="var(--green)"/>
        </svg>
        TOUGH
      </div>
      <div class="feature">
        <svg class="feature-icon" viewBox="0 0 46 46" aria-hidden="true">
          <path d="M12 40 C6 30 8 14 22 6 C26 20 22 34 12 40 Z" fill="var(--green)"/>
          <path d="M16 38 C24 26 34 24 44 26 C38 38 26 42 16 38 Z" fill="var(--green)"/>
        </svg>
        BIODEGRADABLE
      </div>
    </div>

    <div class="tagline">GENTLE ON SKIN.<br>EASY ON THE ENVIRONMENT</div>

    <footer class="bottom-band">
      <p class="slogan">Clean Germ Free. Guilt Free</p>
    </footer>
  </main>
</body>
</html>
```